Hello my name is Colin, I am Starting a business called Harbor Health and fitness and am in need of a memorable business card.
It is a personal training studio. I have added the logo that i would like to be on the left center om my business card. i would like room left up the top for a heading sentence such as. "Is your body shocking for all the wrong reasons". there must be room left on the right of the logo below the main heading for 3 sub headings.
then under those 3 headings and logo room for another larger heading eg. "give me a call and learn how to eat chocolate, drink bear and have great sex". in what room is left i would like to be used for my contact details, use I'm Colin Pettersby your fitness expert on the left then on the right Phone, Email and website space in at least 12 Point. Very specific i know :) now onto the back, for the back i would like an eye catching graphic and room for one main headline and 3 bullet points centered just write anything i will choose what to put in them when i pick a winner. Thank you very much for sticking through all of that :) i appreciate you taking the time to read it and hopefully undergo designing me a business card.
I can't wait to see the designs!

Target Market(s)

slightly more towards females although it would probably be best if it was targeted towards both sexes

Industry/Entity Type

Training

Requirements
Nice to have
• I would love to see if anyone could come up with a design that would really make my card stand out and be memorable.
Should not have
• tacky fitness photos of abs and muscles etc.

```html
<!DOCTYPE html>
<html lang="en">
<head>
<meta charset="utf-8">
<title>Harbor Health and Fitness – Business Card Set</title>
<link rel="stylesheet" href="https://fonts.googleapis.com/css2?family=Arimo:wght@400;700&family=Jost:wght@400;500;600&display=swap">
<style>
  :root {
    --stage: #6a4330;
    --paper: #ffffff;
    --brand-blue: #1f5a94;
    --ink-navy: #1b3f6b;
    --ink-grey: #555a60;
    --ink-dark: #111111;
    --panel-top: #0f3a66;
    --panel-bottom: #1b5591;
    --divider: #1b3f6b;
    --pattern-base: #f3e6e0;
    --pattern-soft: #e9d4cc;
    --mark-faint: rgba(150, 165, 195, 0.22);
    --mark-faint-dark: rgba(160, 185, 220, 0.22);
    --card-shadow: 0 3px 8px rgba(0, 0, 0, 0.45);
  }
  * { box-sizing: border-box; margin: 0; padding: 0; }
  html, body { width: 1200px; height: 745px; overflow: hidden; }
  body { background: var(--stage); position: relative; font-family: "Arimo", Arial, sans-serif; }

  .card { position: absolute; width: 524px; height: 298px; box-shadow: var(--card-shadow); overflow: hidden; }
  .card--front { left: 56px; top: 58px; background: var(--paper); }
  .card--pattern { left: 604px; top: 60px; }
  .card--white { left: 56px; top: 394px; background: var(--paper); }
  .card--navy { left: 615px; top: 400px; background: linear-gradient(180deg, var(--panel-top), var(--panel-bottom)); }

  /* Front card */
  .front__info { position: absolute; left: 0; top: 0; width: 266px; height: 100%; }
  .front__info > * { position: absolute; left: 12px; }
  .front__divider { position: absolute; left: 266px; top: 0; width: 6px; height: 100%; background: var(--paper); border-left: 3px solid var(--divider); }
  .front__panel { position: absolute; left: 272px; top: 0; right: 0; height: 100%;
    background: linear-gradient(180deg, var(--panel-top), var(--panel-bottom)); color: #fff; }
  .front__panel > * { position: absolute; left: 13px; }

  .tagline { top: 11px; color: var(--brand-blue); font-size: 19px; line-height: 23px; }
  .brand { top: 66px; color: var(--brand-blue); font-family: "Jost", sans-serif; font-weight: 400; display: flex; align-items: center; gap: 8px; }
  .brand__dot { width: 22px; height: 22px; border-radius: 50%; background: var(--brand-blue); flex: none; }
  .brand__name { font-size: 64px; line-height: 70px; }
  .brand__sub { top: 140px; left: auto !important; right: 14px; color: var(--brand-blue); font-family: "Jost", sans-serif; font-weight: 400; font-size: 19px; line-height: 22px; }

  .person { top: 180px; }
  .person__name { color: var(--ink-navy); font-weight: 700; font-size: 20px; line-height: 24px; }
  .person__role { color: var(--ink-grey); font-size: 16px; line-height: 20px; }
  .contact { top: 234px; list-style: none; color: var(--ink-grey); font-size: 17px; }
  .contact li { display: flex; align-items: center; gap: 6px; height: 28px; }
  .contact svg { width: 16px; height: 16px; fill: var(--ink-navy); }

  .panel__lead { top: 18px; font-family: "Jost", sans-serif; font-size: 17px; line-height: 21px; }
  .panel__list { top: 86px; list-style: none; font-family: "Jost", sans-serif; font-size: 17px; }
  .panel__list li { height: 26px; line-height: 26px; display: flex; align-items: center; gap: 6px; }
  .panel__list li::before { content: ""; width: 6px; height: 6px; border-radius: 50%; background: #fff; }
  .panel__offer { top: 187px; letter-spacing: 0.5px; font-size: 18px; line-height: 24.5px; }

  /* Backs */
  .back { position: absolute; inset: 0; font-family: "Jost", sans-serif; text-align: center; }
  .back__headline { font-size: 25px; line-height: 30px; margin-top: 84px; }
  .back__list { list-style: none; display: inline-block; text-align: left; font-size: 26px; line-height: 30px; margin-top: 4px; }
  .back__list li { display: flex; align-items: center; gap: 8px; }
  .back__list li::before { content: ""; width: 11px; height: 11px; border-radius: 50%; background: currentColor; flex: none; }
  .back__url { position: absolute; left: 0; right: 0; bottom: 18px; font-size: 21px; font-weight: 500; letter-spacing: 3.5px; }

  .pattern-fill { position: absolute; inset: 0;
    background: radial-gradient(circle at 50% 45%, var(--pattern-base), var(--pattern-soft)); }
  .card--pattern .back { color: var(--ink-dark); }
  .card--white .back { color: var(--ink-grey); }
  .card--navy .back { color: #fff; }

  .watermark { position: absolute; left: 40px; top: 55px; font-family: "Jost", sans-serif; font-weight: 400; line-height: 1; }
  .watermark__name { font-size: 130px; }
  .watermark__sub { font-size: 34px; text-align: right; padding-right: 10px; }
  .card--white .watermark { color: var(--mark-faint); }
  .card--navy .watermark { color: var(--mark-faint-dark); }
</style>
</head>
<body>

<section class="card card--front" aria-label="Card front">
  <div class="front__info">
    <p class="tagline">Is your body shocking for<br>all the wrong reasons</p>
    <div class="brand"><span class="brand__dot"></span><span class="brand__name">Harbor</span></div>
    <span class="brand__sub">Health and Fitness</span>
    <div class="person">
      <p class="person__name">Colin Pettersby</p>
      <p class="person__role">Fitness expert</p>
    </div>
    <ul class="contact">
      <li><svg viewBox="0 0 16 16" aria-hidden="true"><path d="M3.5 1.5l2.5 0 1 3.5-1.6 1.2c.8 1.7 2 2.9 3.6 3.6l1.2-1.6 3.5 1v2.5c0 .8-.7 1.5-1.5 1.5C6.6 13.2 2.8 9.4 2 3c0-.8.7-1.5 1.5-1.5z"/></svg>012-555-0147</li>
      <li><svg viewBox="0 0 16 16" aria-hidden="true"><path d="M1 4h14v9H1z M2 5l6 4 6-4" fill="none" stroke="#1b3f6b" stroke-width="1.6"/></svg>name@harborhealth.com</li>
    </ul>
  </div>
  <div class="front__divider"></div>
  <div class="front__panel">
    <p class="panel__lead">Lorem Ispum Lorem Ispum<br>Lorem Ispum</p>
    <ul class="panel__list">
      <li>Lorem ipsum diet</li>
      <li>Lorem ipsum diet</li>
      <li>Lorem ipsum diet</li>
    </ul>
    <p class="panel__offer">Give me a call and learn<br>How to eat chocolate<br>Drink bear<br>Have great sex</p>
  </div>
</section>

<section class="card card--pattern" aria-label="Card back, patterned">
  <div class="pattern-fill" role="img" aria-label="Soft blush paisley and floral ornament pattern"></div>
  <div class="back">
    <p class="back__headline">Lorem Ispum Lorem Ispum Lorem Ispum</p>
    <ul class="back__list">
      <li>Lorem Ispum Lorem</li>
      <li>Lorem Ispum Lorem</li>
      <li>Lorem Ispum Lorem</li>
    </ul>
    <p class="back__url">www.harborhealth.com</p>
  </div>
</section>

<section class="card card--white" aria-label="Card back, white">
  <div class="watermark" aria-hidden="true">
    <div class="watermark__name">Harbor</div>
    <div class="watermark__sub">Health and Fitness</div>
  </div>
  <div class="back">
    <p class="back__headline">Lorem Ispum Lorem Ispum Lorem Ispum</p>
    <ul class="back__list">
      <li>Lorem Ispum Lorem</li>
      <li>Lorem Ispum Lorem</li>
      <li>Lorem Ispum Lorem</li>
    </ul>
    <p class="back__url">www.harborhealth.com</p>
  </div>
</section>

<section class="card card--navy" aria-label="Card back, navy">
  <div class="watermark" aria-hidden="true">
    <div class="watermark__name">Harbor</div>
    <div class="watermark__sub">Health and Fitness</div>
  </div>
  <div class="back">
    <p class="back__headline">Lorem Ispum Lorem Ispum Lorem Ispum</p>
    <ul class="back__list">
      <li>Lorem Ispum Lorem</li>
      <li>Lorem Ispum Lorem</li>
      <li>Lorem Ispum Lorem</li>
    </ul>
    <p class="back__url">www.harborhealth.com</p>
  </div>
</section>

</body>
</html>
```